Velmira Body Oil Label for 4 -8 oz bottles

We are selling 4 and 8 oz body oils and need a label to put on our bottles. I'm not sure if we want a label for the front and also the back of the bottle or just one label in the front. You can give me examples of each way. Attached is our logo on a blue background but the background will change colors depending on the scent as specified in the design description. Our bottle will be either clear or white with a pump spray type lid as shown in the attached example. Attached are also our design criteria which is needed for the labels.
Updates

We have decided to use the disc top cap and not the pump spray cap. If you are able to, please show us the design on the 4 oz bottle with the disc top cap. Thanks

Target Market(s)

women

Industry/Entity Type

skincare, cosmetics

Font styles to use
Serif
Sans Serif

Requirements
Must have
• stylish name for each scented oil which contrasts the font in the logo. Also must have darker colors since the logo colors are lighter.
Nice to have
• Border around the labels, maybe one solid color or maybe two complimenting colors which go well with the fragrnace name
Should not have
• background colors that match the logo colors

```html
<!DOCTYPE html>
<html lang="en">
<head>
<meta charset="utf-8">
<title>Velmira Cotton Candy Body Oil Label</title>
<link rel="stylesheet" href="https://fonts.googleapis.com/css2?family=Anton&family=Delius+Swash+Caps&family=Source+Sans+3:wght@400;600;700&display=swap">
<style>
  :root {
    --orchid: #c05ba2;
    --lagoon: #1bbec6;
    --paper: #ffffff;
    --ink: #1a1a1a;
    --backdrop: #dcdcdc;
    --text-sans: "Source Sans 3", "Helvetica Neue", Arial, sans-serif;
    --text-display: "Anton", "Impact", sans-serif;
    --text-flourish: "Delius Swash Caps", "Comic Sans MS", cursive;
  }
  * { margin: 0; padding: 0; box-sizing: border-box; }
  html, body {
    width: 1200px; height: 1200px; overflow: hidden;
    background: var(--backdrop);
    font-family: var(--text-sans);
  }
  .canvas { position: relative; width: 1200px; height: 1200px; }

  .label { position: absolute; top: 97px; width: 403px; height: 1006px; }

  /* Front label */
  .label-front { left: 137px; background: var(--paper); }
  .brand-tab {
    position: absolute; left: 45px; top: 0; width: 313px; height: 217px;
    background: var(--orchid);
    border-radius: 0 0 26px 26px;
    display: flex; align-items: center; justify-content: center; gap: 14px;
  }
  .brand-dot { width: 16px; height: 16px; border-radius: 50%; background: var(--paper); }
  .brand-name {
    font-family: var(--text-sans); font-weight: 400;
    font-size: 50px; color: var(--paper); letter-spacing: 1px;
  }
  .scent-band {
    position: absolute; left: 0; top: 298px; width: 100%; height: 392px;
    background: linear-gradient(to bottom,
      var(--orchid) 0, var(--orchid) 245px,
      var(--lagoon) 245px, var(--lagoon) 380px,
      var(--orchid) 380px, var(--orchid) 392px);
  }
  .scent-name {
    position: absolute; left: 0; top: 50px; width: 100%;
    text-align: center; color: var(--paper);
    font-family: var(--text-display); font-size: 112px;
    line-height: 96px; letter-spacing: 1px; text-transform: uppercase;
  }
  .product-type {
    position: absolute; left: 0; top: 300px; width: 100%;
    text-align: center; color: var(--paper);
    font-family: var(--text-flourish); font-size: 44px; line-height: 50px;
  }
  .benefits {
    position: absolute; left: 0; top: 748px; width: 100%;
    list-style: none; text-align: center;
    font-size: 17px; font-weight: 600; color: var(--ink); line-height: 34px;
  }
  .net-tab {
    position: absolute; left: 45px; bottom: 0; width: 313px; height: 108px;
    background: var(--orchid); border-radius: 26px 26px 0 0;
    display: flex; align-items: center; justify-content: center;
    color: var(--paper); font-weight: 700; font-size: 17px;
  }

  /* Back label */
  .label-back { left: 661px; background: var(--lagoon); color: var(--paper); }
  .info-block { position: absolute; left: 51px; width: 320px; font-size: 17.5px; line-height: 23.8px; }
  .info-block h2 { font-size: 17.5px; font-weight: 700; line-height: 23.8px; }
  .info-ingredients { top: 88px; }
  .info-directions { top: 322px; }
  .info-warnings { top: 462px; }
  .info-warnings ul { list-style: none; }
  .distributor {
    position: absolute; left: 66px; top: 717px; width: 271px; height: 208px;
    background: var(--paper); color: var(--ink);
    text-align: center; font-size: 17px; line-height: 23px; padding-top: 21px;
  }
  .distributor .made-in { margin-top: 49px; }
  .distributor .net-weight { font-weight: 700; }
</style>
</head>
<body>
<main class="canvas">

  <section class="label label-front" aria-label="Front label">
    <div class="brand-tab">
      <span class="brand-dot"></span>
      <span class="brand-name">Velmira</span>
    </div>
    <div class="scent-band">
      <h1 class="scent-name">Cotton<br>Candy</h1>
      <p class="product-type">Body Oil</p>
    </div>
    <ul class="benefits">
      <li>Non-Greesy</li>
      <li>With Vitamin E</li>
      <li>Ultra Moisturizing</li>
    </ul>
    <div class="net-tab">Net Wt. 4 fl. oz. (118 mL)</div>
  </section>

  <section class="label label-back" aria-label="Back label">
    <div class="info-block info-ingredients">
      <h2>Ingredients</h2>
      <p>Cocos Nucifera (Coconut) Oil, Prunus Amygdalus Dulcis (Almond) Oil, Vitis Vinifera (Grapeseed) Oil, Sesamum Indicum (Sesame) Seed Oil, Simmondsia Chinensis (Jojoba) Oil, Tocopheryl Acetate (Vitamin E). Essential oils, and fragrances.</p>
    </div>
    <div class="info-block info-directions">
      <h2>Directions</h2>
      <p>Apply a small amount to skin and massage until absorbed. Use daily for best results.</p>
    </div>
    <div class="info-block info-warnings">
      <h2>Warnings / Disclaimers</h2>
      <ul>
        <li>- For external use only.</li>
        <li>- Avoid contact with eyes.</li>
        <li>- Discontinue use if irritation occurs.</li>
        <li>- Keep out of reach of children.</li>
        <li>- Contains nut oils — use with caution if you have nut allergies.</li>
      </ul>
    </div>
    <div class="distributor">
      <p>Distributed by Velmira</p>
      <p>482 Larkspur Lane</p>
      <p>Alder Springs, CO 80455</p>
      <p class="made-in">Made in USA</p>
      <p class="net-weight">Net Wt. 4 fl. oz. (118 mL)</p>
    </div>
  </section>

</main>
</body>
</html>
```